Geschäftspapiere für unternehmerische Holding für Beteiligungen, Projektgesellschaften und kaufmännische Steuerung
Zielgruppe
Die Hollwen GmbH ist eine unternehmerische Holding für Beteiligungen, Projektgesellschaften und kaufmännische Steuerung. Sie übernimmt Management-, Controlling- und Strukturierungsaufgaben für verbundene Unternehmen.
Zielgruppe sind Banken, Investoren, Geschäftspartner, Steuerberater, Rechtsanwälte, Behörden sowie Geschäftsführungen und Gesellschafter von Beteiligungs- und Projektgesellschaften.
Aufgabenstellung
Gesucht wird ein digitales Briefpapier für die Hollwen GmbH, das sowohl als PDF/Dokumentvorlage als auch beim Ausdruck professionell funktioniert.
Wichtig ist ein sehr klarer, hochwertiger und seriöser Auftritt. Das Design soll reduziert, strukturiert und geschäftlich wirken – keine verspielten Elemente, keine überladenen Grafiken, keine auffälligen Muster.
Das Briefpapier muss drucktauglich sein. Bitte ausreichende Druckränder und Sicherheitsabstände berücksichtigen, damit Kopf- und Fußbereich auch auf normalen Büro- und Laserdruckern sauber ausgegeben werden können. Das Layout soll sowohl digital als auch gedruckt stimmig aussehen.
Format: DIN A4 Hochformat.
Gewünschte Inhalte:
* Logo der Hollwen GmbH
* Firmenname: Hollwen GmbH
* Geschäftsanschrift: Lindauer Weg 52, 80339 München
* Telefon: 089 58210946
* E-Mail: info@hollwenbeta.example
* Webseite: hollwenbeta.example
* Geschäftsführung: Dipl.-Wirtschaftsing. (FH) Till Osterwald
* Registergericht / Amtsgericht München HRB 527081
* Bankverbindung IBAN DE918204 5571 0009 1826 40
Besonderer Wert liegt auf:
* hochwertiger Holding-/Investment-Anmutung
* sehr guter Lesbarkeit
* klarer Kopf- und Fußzeile
* sauberer Typografie
* professioneller Nutzbarkeit für Angebote, Verträge, Behörden- und Bankkorrespondenz
Bitte das Design so anlegen, dass es später als editierbare Word-/PDF-Vorlage genutzt werden kann und sowohl das Logo, als auch die Farben entsprechend verwenden.

```html
<!DOCTYPE html>
<html lang="de">
<head>
<meta charset="utf-8">
<title>Hollwen GmbH – Briefpapier</title>
<link href="https://fonts.googleapis.com/css2?family=Montserrat:wght@400;500&display=swap" rel="stylesheet">
<style>
  :root {
    --navy: #141b2d;
    --ink: #1d1d1f;
    --rule: #a6a6a6;
    --icon: #8c8c8c;
    --logo-text: #c9cbd0;
    --sig: #e3ebf6;
    --page: #ffffff;
  }
  * { margin: 0; padding: 0; box-sizing: border-box; }
  html, body { width: 849px; height: 1200px; overflow: hidden; background: var(--page); }
  body { font-family: "Montserrat", sans-serif; color: var(--ink); }
  .sheet { position: relative; width: 849px; height: 1200px; border: 1px solid var(--rule); }

  .logo-block {
    position: absolute; left: 102px; top: 38px; width: 157px; height: 57px;
    background: var(--navy);
    display: flex; align-items: flex-end; justify-content: center; padding-bottom: 8px;
  }
  .logo-name {
    font-weight: 400; font-size: 21px; letter-spacing: 1px; color: var(--logo-text);
  }
  .header-claim {
    position: absolute; left: 279px; top: 82px;
    font-size: 13.4px; letter-spacing: 2.6px; font-weight: 400;
  }
  .rule { position: absolute; left: 100px; width: 670px; height: 0; border-top: 1px solid var(--rule); }
  .rule--top { top: 105px; }
  .rule--bottom { top: 1157px; }

  .sender-line { position: absolute; left: 105px; top: 208px; font-size: 10px; }
  .fold-mark { position: absolute; left: 3px; top: 427px; width: 39px; border-top: 1px solid var(--rule); }
  .punch-mark { position: absolute; left: 70px; top: 438px; width: 6px; height: 6px; background: var(--rule); }

  .letter { position: absolute; left: 102px; top: 434px; width: 670px; font-size: 14.6px; line-height: 20px; }
  .letter p { margin-bottom: 20px; }
  .closing { position: absolute; left: 102px; top: 734px; font-size: 14.6px; }
  .signature { position: absolute; left: 107px; top: 760px; width: 266px; height: 36px; background: var(--sig); }
  .signer { position: absolute; left: 102px; top: 834px; font-size: 14.6px; }

  .footer { position: absolute; top: 1074px; left: 0; width: 849px; font-size: 11px; line-height: 13px; }
  .footer-item { position: absolute; display: flex; }
  .footer-item svg { position: absolute; left: -22px; top: -1px; }
</style>
</head>
<body>
<div class="sheet">
  <div class="logo-block"><span class="logo-name">HOLLWEN</span></div>
  <div class="header-claim">HOLLWEN GMBH PRIVATE INVESTMENT HOLDING</div>
  <div class="rule rule--top"></div>

  <div class="sender-line">HOLLWEN GMBH, Lindauer Weg 52, 80339 München</div>
  <div class="fold-mark"></div>
  <div class="punch-mark"></div>

  <div class="letter">
    <p>Sehr geehrte Damen ubd Herren</p>
    <p>dolor sit amet, consetetur sadipscing elitr, sed diam nonumy eirmod tempor invidunt ut labore et dolore magna aliquyam erat, sed diam voluptua. At vero eos et accusam</p>
    <p>nonumy eirmod tempor invidunt ut labore et dolore magna aliquyam erat, sed diam voluptua. sed diam nonumy eirmod tempor invidunt ut labore et dolore magna amet, aliquyam erat, sed diam voluptua. At vero eos et accusam et justo dolor sit amet, conse­tetur consetetur sadipscing elitr, sed diam nonumy eirmod tempor invidunt ut labdol­magna aliquyam erat, sed diam voluptua. At vero eos et accusam et justo dolor sit amet, consetetu At vero eos et accusam et justo dolor sit amet, conseteturdolor sit amet, consetetur sadipscing elitr, sed diam</p>
  </div>
  <div class="closing">Mit freundlichen Grüßen</div>
  <div class="signature" role="img" aria-label="Handschriftliche Unterschrift von Till Osterwald"></div>
  <div class="signer">Till Osterwald</div>

  <div class="footer">
    <div class="footer-item" style="left:132px;top:0">
      <svg width="18" height="18" viewBox="0 0 18 18"><circle cx="9" cy="9" r="8" fill="none" stroke="var(--icon)"/><circle cx="9" cy="7" r="2.6" fill="var(--icon)"/><path d="M4.5 14c.8-3 2.3-4 4.5-4s3.7 1 4.5 4z" fill="var(--icon)"/></svg>
      <div>Dipl.-Wirtschaftsing. (FH)<br>Till Osterwald</div>
    </div>
    <div class="footer-item" style="left:132px;top:39px">
      <svg width="18" height="18" viewBox="0 0 18 18"><circle cx="9" cy="9" r="8" fill="none" stroke="var(--icon)"/><path d="M9 14s-3.5-3.6-3.5-6a3.5 3.5 0 0 1 7 0c0 2.4-3.5 6-3.5 6z" fill="var(--icon)"/><circle cx="9" cy="8" r="1.3" fill="#fff"/></svg>
      <div>Lindauer Weg 52<br>80339 München</div>
    </div>
    <div class="footer-item" style="left:364px;top:0">
      <svg width="18" height="18" viewBox="0 0 18 18"><circle cx="9" cy="9" r="8" fill="none" stroke="var(--icon)"/><path d="M6 5.5l1.6-.4 1 2-1 .8c.4 1 1.2 1.8 2.2 2.2l.8-1 2 1-.4 1.6c-3 .2-6.4-3.2-6.2-6.2z" fill="var(--icon)"/></svg>
      <div>089 58210946</div>
    </div>
    <div class="footer-item" style="left:364px;top:26px">
      <svg width="18" height="18" viewBox="0 0 18 18"><circle cx="9" cy="9" r="8" fill="none" stroke="var(--icon)"/><text x="9" y="12.2" font-size="9" text-anchor="middle" fill="var(--icon)" font-family="Montserrat, sans-serif">@</text></svg>
      <div>info@hollwenbeta.example</div>
    </div>
    <div class="footer-item" style="left:364px;top:52px">
      <svg width="18" height="18" viewBox="0 0 18 18"><circle cx="9" cy="9" r="8" fill="none" stroke="var(--icon)"/><circle cx="9" cy="9" r="4.3" fill="none" stroke="var(--icon)" stroke-width=".8"/><path d="M4.7 9h8.6M9 4.7v8.6" stroke="var(--icon)" stroke-width=".7"/></svg>
      <div>hollwenbeta.example</div>
    </div>
    <div class="footer-item" style="left:552px;top:0">
      <svg width="18" height="18" viewBox="0 0 18 18"><circle cx="9" cy="9" r="8" fill="none" stroke="var(--icon)"/><path d="M9 5v8M5 7h8M5 7l-1.5 3h3zM13 7l-1.5 3h3zM6.5 13h5" stroke="var(--icon)" stroke-width=".8" fill="none"/></svg>
      <div>Registergericht / Amtsgericht München<br>HRB 527081</div>
    </div>
    <div class="footer-item" style="left:552px;top:39px">
      <svg width="18" height="18" viewBox="0 0 18 18"><circle cx="9" cy="9" r="8" fill="none" stroke="var(--icon)"/><path d="M4.5 7.5L9 4.8l4.5 2.7zM5.5 8.2h7M6 8.5v3.5M8 8.5v3.5M10 8.5v3.5M12 8.5v3.5M5 12.6h8" stroke="var(--icon)" stroke-width=".9" fill="var(--icon)"/></svg>
      <div>IBAN DE91 8204 5571 0009 1826 40</div>
    </div>
  </div>
  <div class="rule rule--bottom"></div>
</div>
</body>
</html>
```